New Web-Page Design Required

We need a new or initial web design for our page vorlan-grid.com. We provide products & services around infrastructure products. We have two products at the moment, but another 2 in the pipeline.
We want to have the following page structure (and part of the project is to design the 7 pages):
- Home
- Products
-One page per product
- Service
- Support
- About
- Contact (Email form)
The start page should include the following information:
- Tweetline / Linkedin Links
- Telephone / Email or in general contact details
- News
- Maybe a link-box, where we can highlight/showcase things
- Link to our support portal, quite prominent
- Testimonials
It would be nice if the product pages would have a image header, where we can put up a screenshot or something. Links to datasheet and videos of the product would be nice as well.
We like the "big banner in the middle" designs, like these two Joomla examples. No need to copy them, it should just give you an idea.
http://www.pelmorthemes.com/itempreview/185
http://www.pelmorthemes.com/content/asj42/index.php
Budget for images available, so please use placeholders or ask us for specific photos/images, if you need them for your design.
Target Market(s)
Business-2-Business, Decision makers and Technical Leads
Industry/Entity Type
News
Look and feel

```html
<!DOCTYPE html>
<html lang="en">
<head>
<meta charset="utf-8">
<title>Vorlan-Grid — Home</title>
<link href="https://fonts.googleapis.com/css2?family=Open+Sans:wght@400;600;700&family=Oswald:wght@600;700&display=swap" rel="stylesheet">
<style>
:root{
  --page:#f1f1f1;
  --outer:#ffffff;
  --teal:#128ea3;
  --teal-light:#1fa8bd;
  --teal-dark:#0b6a82;
  --ink:#333333;
  --grey:#555555;
  --slider:#3c3c3c;
  --card:#efefef;
  --footer:#222222;
  --footer-base:#141414;
  --footer-text:#8a8a8a;
}
*{margin:0;padding:0;box-sizing:border-box}
html,body{width:1113px;height:1200px;overflow:hidden;background:var(--outer)}
body{font-family:"Open Sans",Verdana,sans-serif;color:var(--ink);position:relative}
.abs{position:absolute}
.page{left:29px;top:0;width:1055px;height:1200px;background:var(--page)}
.map-backdrop{left:60px;top:190px;width:990px;height:560px;border-radius:40%;
  background:radial-gradient(ellipse at center,rgba(170,170,170,.35),rgba(241,241,241,0) 70%)}
.logo-mark{left:196px;top:36px;width:52px;height:52px;border-radius:50%;background:var(--teal)}
.logo-name{left:258px;top:38px;font-size:36px;font-weight:600;color:#4a4a4a;letter-spacing:-.5px}
.contact{left:806px;top:48px;font-size:10px;line-height:14px;color:#444}
.contact .phone{font-size:13px;line-height:18px;color:#333}
.nav{left:349px;top:118px;display:flex;gap:26px;font-size:11.5px;color:#444;letter-spacing:.2px}
.nav-dot{left:361px;top:139px;width:7px;height:7px;border-radius:50%;background:var(--teal)}
.slider{left:196px;top:156px;width:722px;height:362px;background:var(--slider)}
.slide-card{left:245px;top:203px;width:622px;height:269px;border-radius:6px;background:var(--card)}
.slide-title{left:263px;top:210px;font-family:"Oswald",sans-serif;font-weight:700;font-size:35px;line-height:40px;color:#444;letter-spacing:.3px}
.slide-title em{font-style:normal;color:var(--teal)}
.slide-text{left:262px;top:302px;width:260px;font-size:9.6px;line-height:11px;text-align:justify;color:#222}
.btn{display:block;height:17px;line-height:17px;font-size:8.5px;color:#fff;background:var(--teal);text-align:center;text-transform:uppercase}
.btn-dark{background:#111}
.slide-photo{left:520px;top:258px;width:340px;height:207px;background:linear-gradient(90deg,rgba(239,239,239,0),#cfcfcf 40%,#b9b9b9)}
.arrow{width:23px;height:23px;border-radius:50%;background:#fff}
.dots{left:530px;top:489px;display:flex;gap:8px}
.dots span{width:7px;height:7px;border-radius:50%;background:#fff}
.box{width:212px;height:272px;top:538px;background:#f6f6f6;box-shadow:0 1px 3px rgba(0,0,0,.12)}
.box-head,.side-head{height:38px;line-height:38px;text-align:center;color:#fff;font-weight:700;font-size:13px;letter-spacing:.5px;background:linear-gradient(var(--teal-light),var(--teal))}
.box-img{position:absolute;left:12px;top:53px;width:186px;height:113px}
.box-text{position:absolute;left:12px;top:178px;width:188px;font-size:9.6px;line-height:11px;text-align:justify;color:#555}
.box .btn{position:absolute;right:13px;top:241px;width:61px}
.intro-title{left:196px;top:836px;font-size:20px;font-weight:700;color:var(--teal-dark);letter-spacing:.2px}
.intro-text{left:196px;top:874px;width:457px;font-size:9.6px;line-height:11.4px;text-align:justify;color:#555}
.intro-text p+p{margin-top:11px}
.side{left:687px;top:832px;width:211px;height:184px;background:#f6f6f6;box-shadow:0 1px 3px rgba(0,0,0,.12)}
.side-list{padding:6px 13px;font-size:9.6px;line-height:11px}
.side-list dt{color:#111}
.side-list dd{color:var(--teal);margin-bottom:10px}
.footer{left:29px;top:1028px;width:1055px;height:144px;background:var(--footer)}
.footer-base{left:29px;top:1172px;width:1055px;height:28px;background:var(--footer-base)}
.fcol{top:1054px;font-size:8px;color:var(--footer-text)}
.fcol h4{color:#eee;font-weight:600;font-size:8px;margin-bottom:8px}
.fcol li{list-style:none;line-height:18.4px}
.copyright{left:29px;top:1179px;width:1055px;text-align:center;font-size:7.5px;color:#888}
</style>
</head>
<body>
<div class="abs page"></div>
<div class="abs map-backdrop" role="img" aria-label="Faint grey world map backdrop"></div>

<header>
  <div class="abs logo-mark"></div>
  <div class="abs logo-name">vorlan·grid</div>
  <div class="abs contact">Happy to help !<br>info@vorlan-grid.com<br><span class="phone">088 40213366512</span></div>
  <nav class="abs nav"><span>HOME</span><span>PRODUCTS</span><span>SERVICES</span><span>SUPPORT</span><span>ABOUT</span><span>CONTACT</span></nav>
  <div class="abs nav-dot"></div>
</header>

<section class="hero">
  <div class="abs slider"></div>
  <div class="abs slide-card"></div>
  <h1 class="abs slide-title"><em>WE COMMIT</em> TO WHAT OTHERS<br>WALK AWAY FROM</h1>
  <p class="abs slide-text">Vorlan-Grid was born from a solid infrastructure, management, automation and highly secure environment experience. With software architecture, design, coding and testing that reaches a combined 30+years experience for a young company. Lessons learned including what not to do.</p>
  <a class="abs btn" style="left:460px;top:374px;width:61px">Read more</a>
  <div class="abs slide-photo" role="img" aria-label="Photo of a business team joining hands in a circle"></div>
  <svg class="abs arrow" style="left:211px;top:325px" viewBox="0 0 23 23"><circle cx="11.5" cy="11.5" r="11.5" fill="#fff"/><path d="M13.5 7 9 11.5 13.5 16z" fill="#222"/></svg>
  <svg class="abs arrow" style="left:879px;top:325px" viewBox="0 0 23 23"><circle cx="11.5" cy="11.5" r="11.5" fill="#fff"/><path d="M9.5 7 14 11.5 9.5 16z" fill="#222"/></svg>
  <div class="abs dots"><span></span><span></span><span></span><span></span></div>
</section>

<section class="features">
  <article class="abs box" style="left:215px">
    <h2 class="box-head">PRODUCTS</h2>
    <div class="box-img" role="img" aria-label="Tablet showing a dashboard on a desk" style="background:linear-gradient(135deg,#8a7a6a,#2b2f33 55%,#cfd3d6)"></div>
    <p class="box-text">Our understanding for customer needs combined with our software development experience, enables us to provide products of outstanding quality.to provide products.</p>
    <a class="btn">Read more</a>
  </article>
  <article class="abs box" style="left:451px">
    <h2 class="box-head">SUPPORT</h2>
    <div class="box-img" role="img" aria-label="Support agent wearing a headset" style="background:linear-gradient(90deg,#cfd3d3,#e8dcd2 55%,#f2eeea)"></div>
    <p class="box-text">Our support portal is available 24/7 and personalized support packages can be tailored to your needs. Our support portal is available 24/7 and personalized tailored to your needs.</p>
    <a class="btn">Read more</a>
  </article>
  <article class="abs box" style="left:687px">
    <h2 class="box-head">SERVICES</h2>
    <div class="box-img" role="img" aria-label="Layered diagram of OS, BIOS and API services" style="background:linear-gradient(135deg,#f7f7f7,#e4eef2 50%,#f2f0dc)"></div>
    <p class="box-text">Installation &amp; Professional Services can be provided by us or competent partners. In any case, you will get very experienced software consultants, who can fix every issue.</p>
    <a class="btn">Read more</a>
  </article>
</section>

<section class="intro">
  <h2 class="abs intro-title">We Commit To What Others Walk Away From</h2>
  <div class="abs intro-text">
    <p>Vorlan-Grid was born from a solid infrastructure, management, automation and highly secure environment experience. With software architecture, design, coding and testing that reaches a combined 30+years experience for a young company. Lessons learned including what not to do.</p>
    <p>Our objective is to be a software development house that designs applications using the latest available technologies and coding it on the same basis, focusing primarily on native mobile applications and the integration of these into different enterprise back end systems</p>
  </div>
  <a class="abs btn btn-dark" style="left:581px;top:965px;width:72px">Read more</a>
</section>

<aside class="abs side">
  <h2 class="side-head">VIDEOS &amp; DATASHEET</h2>
  <dl class="side-list">
    <dt>q.Ledger</dt><dd>Dynamic video about our q.Ledger application.</dd>
    <dt>q.Ledger Datasheet</dt><dd>Download the q.Ledger Datasheet.</dd>
    <dt>NTX/C</dt><dd>NTX/C Feature Presentation</dd>
    <dt>NTX/C Datasheet</dt><dd>Download the NTX/C Datasheet</dd>
  </dl>
</aside>

<footer>
  <div class="abs footer"></div>
  <div class="abs fcol" style="left:196px"><h4>About Us</h4><ul><li>dolor sit amet</li><li>sit ut duis</li><li>molestie</li><li>augue homero</li></ul></div>
  <div class="abs fcol" style="left:329px"><h4>Products</h4><ul><li>dolor sit amet</li><li>sit ut duis</li><li>molestie</li><li>augue homero</li></ul></div>
  <div class="abs fcol" style="left:459px"><h4>Client Service</h4><ul><li>dolor sit amet</li><li>sit ut duis</li><li>molestie</li><li>augue homero</li></ul></div>
  <div class="abs fcol" style="left:591px"><h4>Shipping</h4><ul><li>dolor sit amet</li><li>sit ut duis</li><li>molestie</li><li>augue homero</li></ul></div>
  <div class="abs fcol" style="left:722px"><h4>Contact Us</h4><ul><li>dolor sit amet</li><li>sit ut duis</li><li>molestie</li><li>augue homero</li></ul></div>
  <div class="abs fcol" style="left:849px"><h4>Follow Us On</h4><ul><li>Friendbook</li><li>Tweetline</li><li>Our Corner</li><li>Callwave</li></ul></div>
  <div class="abs footer-base"></div>
  <p class="abs copyright">Copyright © 2013 Vorlan-Grid &nbsp; | &nbsp; Kestrel, Lumenwatch are either registered trademarks or trademarks of Kestrel Systems Corporation in the United States and /or other countries &nbsp; | &nbsp; Terms &amp; Condition</p>
</footer>
</body>
</html>
```